RivoCounsel Compensation Lawyers

We need a modern, sleek letterhead that is professional.

In relation to the footer, we would like to have firm contact details there ideally, however you must also insert at the bottom of each page the following....

Liability limited by a scheme approved under the Professional Standards Legislation.

From the attachment you can extract the firm logo. Also, I would like the Accredited specialist circle on the letterhead also.

Also, I would like you to create a document that can easily be edited for change of contact details, as these are likely to change.

Industry/Entity Type

It Professional

Font styles to use
Sans Serif

Colors
0655a3
3276b5
85abd2
0492cd
33a6d7
85cae6
cee9f5
eaf1f7
cbcbcb

Requirements
Must have
• Ph: 8371-5264
• F: 8815-3927
• M 0468-253-914
• mk@rivocounsel.example.au
• www.rivocounsel.example.au
Nice to have
• the word document gives you an idea of what I like. I am happy for your to amaze me with your creativity.

```html
<!DOCTYPE html>
<html lang="en">
<head>
<meta charset="utf-8">
<title>RivoCounsel Compensation Lawyers – Letterhead</title>
<link rel="stylesheet" href="https://fonts.googleapis.com/css2?family=PT+Sans:wght@400;700&family=Didact+Gothic&display=swap">
<style>
  :root {
    --backdrop: #e6e8eb;
    --paper: #ffffff;
    --brand-deep: #0655a3;
    --brand-mid: #3276b5;
    --rule: #33a6d7;
    --seal: #d3dcee;
    --footer-tint: #eaf1f7;
    --ink: #1b1b1b;
    --ink-navy: #1f3a6e;
  }
  * { box-sizing: border-box; margin: 0; padding: 0; }
  html, body { width: 1000px; height: 1200px; overflow: hidden; }
  body { background: var(--backdrop); position: relative; font-family: "PT Sans", sans-serif; }

  .letterhead {
    position: absolute; left: 100px; top: 35px;
    width: 800px; height: 1130px;
    background: linear-gradient(to bottom, var(--paper) 0, var(--paper) 955px, var(--footer-tint) 1130px);
    box-shadow: 0 2px 10px rgba(0,0,0,0.15);
  }

  .brand-name {
    position: absolute; left: 45px; top: 112px;
    font-family: "PT Sans", sans-serif; font-weight: 700;
    font-size: 17px; letter-spacing: 1.2px; text-transform: uppercase;
    color: var(--brand-deep); white-space: nowrap;
  }

  .contact-list {
    position: absolute; right: 29px; top: 44px;
    list-style: none; text-align: right; font-size: 13.5px; line-height: 21.7px;
  }
  .contact-list .label { color: var(--brand-mid); }
  .contact-list .value { color: var(--ink); }

  .rule { position: absolute; left: 33px; width: 737px; height: 1px; background: var(--rule); }
  .rule--top { top: 145px; }
  .rule--bottom { top: 1052px; }

  .accreditation-seal { position: absolute; left: 309px; top: 475px; width: 180px; height: 180px; }

  .footer {
    position: absolute; left: 0; right: 0; top: 1059px;
    text-align: center; font-family: "Didact Gothic", sans-serif;
  }
  .footer .liability { font-size: 16px; color: var(--ink); line-height: 22px; }
  .footer .address, .footer .web { font-size: 15.5px; color: var(--ink-navy); line-height: 21px; }
</style>
</head>
<body>
  <main class="letterhead">
    <div class="brand-name">RivoCounsel Compensation Lawyers</div>

    <ul class="contact-list">
      <li><span class="label">Phone</span><span class="value">: 8371-5264</span></li>
      <li><span class="label">Fax</span><span class="value">: 8815-3927</span></li>
      <li><span class="label">Mobile</span><span class="value">: 0468-253-914</span></li>
      <li><span class="label">Email</span><span class="value">: mk@rivocounsel.example.au</span></li>
    </ul>

    <div class="rule rule--top"></div>

    <svg class="accreditation-seal" viewBox="0 0 180 180" aria-hidden="true">
      <circle cx="90" cy="90" r="85" fill="none" stroke="var(--seal)" stroke-width="5"/>
    </svg>

    <div class="rule rule--bottom"></div>

    <footer class="footer">
      <p class="liability">Liability limited by a scheme approved under the Professional Standards Legislation</p>
      <p class="address">P.O. Box B418 Marlow Vale NSW 2190</p>
      <p class="web">www.rivocounsel.example.au</p>
    </footer>
  </main>
</body>
</html>
```